Dermatologist office in Brasilia. My with "target customers" are specially women.

I’m a dermatologist who works since 2006 in Brasilia. In 2017 I decided to change and improve my career. I decided to work more with cosmetics (Velunex and fillers), I still work with clinical and surgical dermatology.
Most of my patients are women but 20-30% are children and men.
I would like to see designs that use a butterfly and the color aquamarine with details in gold.

Industry/Entity Type

Cosmetics

Font styles to use
Sans Serif

Colors
33b8a4
87cfc6
cfeae6
85cae6

Requirements
Must have
• My project must have my name (Kaede Morinaga) and my medical specialty (Dermatologista)
Nice to have
• The colors I prefer are aquamarine or Corvell Blue Box.
• I also prefer a butterfly that means transformation and a new life.
• I prefer a sofisticated and also minimalist design.

```html
<!DOCTYPE html>
<html lang="en">
<head>
<meta charset="utf-8">
<title>Kaede Morinaga — Stationery</title>
<link href="https://fonts.googleapis.com/css2?family=Work+Sans:wght@300;400;500&family=Roboto+Condensed:wght@400&display=swap" rel="stylesheet">
<style>
  :root {
    --teal: #33b8a4;
    --teal-mid: #87cfc6;
    --teal-pale: #cfeae6;
    --sky: #85cae6;
    --ink: #2b2b2b;
    --body: #5a5a5a;
    --olive: #3d4226;
    --paper: #ffffff;
    --stage: #ffffff;
  }
  * { margin: 0; padding: 0; box-sizing: border-box; }
  html, body { width: 1200px; height: 1200px; overflow: hidden; background: var(--stage); }
  body { position: relative; font-family: "Work Sans", sans-serif; color: var(--body); }

  .sheet { position: absolute; background: var(--paper); box-shadow: 0 6px 18px rgba(0,0,0,.14); overflow: hidden; }
  .abs { position: absolute; }

  /* brand block */
  .brand { position: absolute; text-align: center; color: var(--ink); font-weight: 400; }
  .brand-dot { width: 30px; height: 30px; border-radius: 50%; background: var(--teal); margin: 0 auto 14px; }
  .brand-name { font-size: 15px; letter-spacing: .42em; white-space: nowrap; text-transform: uppercase; }
  .brand-role { font-size: 7px; letter-spacing: .62em; margin-top: 8px; text-transform: uppercase; white-space: nowrap; }

  /* front card */
  .card-front { left: 46px; top: 531px; width: 402px; height: 230px; }
  .card-front .brand { left: 0; width: 214px; top: 70px; }
  .card-front .brand-name { font-size: 13px; letter-spacing: .44em; }
  .card-front .brand-role { font-size: 6px; margin-top: 6px; }
  .card-divider { left: 206px; top: 57px; width: 1px; height: 109px; background: #8a8a8a; }
  .card-info { left: 226px; top: 55px; }
  .card-name { font-family: "Roboto Condensed", sans-serif; font-size: 17px; color: #3a3a3a; text-transform: uppercase; }
  .card-title { font-size: 9.5px; color: var(--teal); margin-top: 2px; }
  .card-address { font-size: 9.5px; line-height: 13px; margin-top: 9px; color: #666; }
  .contact-list { list-style: none; font-size: 9.5px; color: #666; }
  .card-info .contact-list { margin-top: 8px; line-height: 13px; }
  .contact-list li { display: flex; align-items: center; gap: 6px; white-space: nowrap; }
  .contact-list svg { width: 7px; height: 7px; flex: none; }

  .card-wave { left: 0; bottom: 0; width: 402px; height: 34px; }

  /* back card */
  .card-back { left: 46px; top: 810px; width: 402px; height: 229px; }
  .card-back .brand { left: 0; width: 402px; top: 72px; }
  .card-back .brand-name { font-size: 15px; letter-spacing: .5em; margin-left: .5em; }
  .card-back .brand-role { font-size: 6.5px; margin-left: .62em; }

  /* letterhead */
  .letterhead { left: 497px; top: 131px; width: 653px; height: 909px; }
  .letterhead .brand { left: 35px; width: 210px; top: 70px; }
  .letterhead .brand-name { font-size: 16px; letter-spacing: .45em; margin-left: .45em; }
  .letterhead .brand-role { font-size: 7px; margin-top: 9px; }
  .letter-date { right: 34px; top: 120px; font-size: 10.5px; color: #666; }
  .letter-greeting { left: 34px; top: 221px; font-size: 24px; font-weight: 400; color: var(--olive); letter-spacing: .02em; }
  .letter-body { left: 35px; width: 590px; top: 273px; font-size: 10.3px; line-height: 14px; color: #666; font-weight: 400; }
  .letter-body p + p { margin-top: 28px; }
  .letter-body p.short { margin-top: 30px; }
  .signature-mark { left: 41px; top: 681px; width: 46px; height: 20px; background: var(--olive); opacity: .85; border-radius: 3px; }
  .signature-line { left: 39px; top: 711px; width: 107px; height: 1px; background: #999; }
  .signature-label { left: 38px; top: 727px; font-size: 13px; color: #555; }
  .letter-contacts { left: 41px; top: 798px; font-size: 10.3px; line-height: 14.5px; }
  .letter-contacts li { gap: 8px; }
  .letter-address { left: 462px; top: 812px; font-size: 10.3px; line-height: 14px; color: #666; }
  .letter-wave { left: 0; top: 839px; width: 653px; height: 70px; }
</style>
</head>
<body>

  <!-- Business card, front -->
  <section class="sheet card-front" aria-label="Business card front">
    <div class="brand">
      <div class="brand-dot"></div>
      <div class="brand-name">Kaede Morinaga</div>
      <div class="brand-role">Dermatologist</div>
    </div>
    <div class="abs card-divider"></div>
    <div class="abs card-info">
      <div class="card-name">Kaede Morinaga</div>
      <div class="card-title">Dermetologist</div>
      <div class="card-address">148/B Harlow Lane,<br>Downtown,New York, USA</div>
      <ul class="contact-list">
        <li><svg viewBox="0 0 10 10"><path d="M2 1 L4 1 L4.5 3.5 L3.3 4.3 Q4.5 6.5 6 7 L6.7 5.8 L9 6.3 L9 8.5 Q4 9 1.5 3 Z" fill="var(--teal)"/></svg>0437 555 018</li>
        <li><svg viewBox="0 0 10 10"><rect x="1" y="2" width="8" height="6" fill="none" stroke="var(--teal)" stroke-width="1.2"/><path d="M1 2 L5 5.5 L9 2" fill="none" stroke="var(--teal)" stroke-width="1.2"/></svg>info@kaedemorinaga.com.au</li>
        <li><svg viewBox="0 0 10 10"><circle cx="5" cy="5" r="4" fill="var(--teal)"/></svg>www.kaedemorinaga.com.au</li>
      </ul>
    </div>
    <svg class="abs card-wave" viewBox="0 0 402 34" preserveAspectRatio="none" aria-hidden="true">
      <path d="M0 26 Q120 36 230 16 Q310 2 360 6 Q390 10 402 30 L402 34 L0 34 Z" fill="var(--sky)"/>
      <path d="M0 22 Q130 32 240 18 Q320 6 362 9 Q392 14 402 32 L402 34 L0 34 Z" fill="var(--paper)"/>
      <path d="M0 24 Q130 36 250 20 Q330 10 365 12 Q392 16 402 34 L0 34 Z" fill="var(--teal)"/>
    </svg>
  </section>

  <!-- Business card, back -->
  <section class="sheet card-back" aria-label="Business card back">
    <div class="brand">
      <div class="brand-dot"></div>
      <div class="brand-name">Kaede Morinaga</div>
      <div class="brand-role">Dermatologist</div>
    </div>
  </section>

  <!-- Letterhead -->
  <section class="sheet letterhead" aria-label="Letterhead">
    <div class="brand">
      <div class="brand-dot"></div>
      <div class="brand-name">Kaede Morinaga</div>
      <div class="brand-role">Dermatologist</div>
    </div>
    <div class="abs letter-date">Date: 20/10/2017</div>
    <h1 class="abs letter-greeting">HELLO</h1>
    <div class="abs letter-body">
      <p>Lorem ipsum dolor sit amet, tale tamquam accumsan pri ex, vim in assum nulla labitur, populo facilisis voluptatum eu sit. Nam fugit animal habemus ei, vim idque lucilius ex, quo ei sensibus liberavisse. Eruditi phaedrum vituperatori bus te eos. Cetero singulis reformidans nam ne. Has ea exerci timeam. Justo malis no has, sit eu iudicabit quaerend Lorem ipsum dolor sit amet, tale tamquam accumsan pri ex, vim in assum nulla labitur, populo facilisis voluptatum eu sit. Nam fugit animal habemus ei, vim idque lucilius ex, quo ei sensibus liberavisse. Eruditi phaedrum vituperatori bus te eos. Cetero singulis reformidans nam ne. Has ea exerci timeam. Justo malis no has, sit eu iudicabit quaerend eu sit. Nam fugit animal habemus ei, vim idque lucilius ex, quo ei sensibus liberavisse. Eruditi phaedrum vituperatori bus te eos. Cetero singulis reformidans nam ne. Has ea exerci timeam.</p>
      <p>Lorem ipsum dolor sit amet, tale tamquam accumsan pri ex, vim in assum nulla labitur, populo facilisis voluptatum eu sit. Nam fugit animal habemus ei, vim idque lucilius ex, quo ei sensibus liberavisse. Eruditi phaedrum vituperatori bus te eos. Cetero singulis reformidans nam ne. Has ea exerci timeam. Justo malis no has, sit eu iudicabit quaerend Lorem ipsum dolor sit amet, tale tamquam accumsan pri ex, vim in assum nulla labitur, populo facilisis voluptatum eu sit. Nam fugit animal habemus ei, vim idque lucilius ex, quo ei sensibus liberavisse. Eruditi phaedrum vituperatori bus te eos. Cetero singulis reformidans nam ne. Has ea exerci timeam. Justo malis no has, sit eu iudicabit quaerend eu sit. Nam fugit animal habemus ei, vim idque lucilius ex, quo ei sensibus liberavisse. Eruditi phaedrum vituperatori bus te eos. Cetero singulis reformidans nam ne. Has ea exerci timeam. Justo malis no has, sit eu iudicabit quaerend Lorem ipsum dolor sit amet, tale.</p>
      <p class="short">Nam fugit animal habemus ei, vim idque lucilius ex, quo ei sensibus liberavisse. Eruditi phaedrum vituperatori<br>bus te eos. Cetero singulis reformidans nam ne. Has ea exerci timeam. Justo malis no has, sit eu iudicabit quaerend Lorem ipsum dolor sit amet, tale</p>
    </div>
    <div class="abs signature-mark" role="img" aria-label="Handwritten signature"></div>
    <div class="abs signature-line"></div>
    <div class="abs signature-label">Signature</div>
    <ul class="abs contact-list letter-contacts">
      <li><svg viewBox="0 0 10 10"><path d="M2 1 L4 1 L4.5 3.5 L3.3 4.3 Q4.5 6.5 6 7 L6.7 5.8 L9 6.3 L9 8.5 Q4 9 1.5 3 Z" fill="var(--teal)"/></svg>0437 555 018</li>
      <li><svg viewBox="0 0 10 10"><rect x="1" y="2" width="8" height="6" fill="none" stroke="var(--teal)" stroke-width="1.2"/><path d="M1 2 L5 5.5 L9 2" fill="none" stroke="var(--teal)" stroke-width="1.2"/></svg>info@merrowindclinic.com.au</li>
      <li><svg viewBox="0 0 10 10"><circle cx="5" cy="5" r="4" fill="none" stroke="var(--teal)" stroke-width="1.2"/><path d="M1 5 H9 M5 1 Q2.5 5 5 9 M5 1 Q7.5 5 5 9" fill="none" stroke="var(--teal)" stroke-width=".9"/></svg>www.merrowindclinic.com.au</li>
    </ul>
    <div class="abs letter-address">148/B Harlow Lane, Downtown,<br>New York, USA</div>
    <svg class="abs letter-wave" viewBox="0 0 653 70" preserveAspectRatio="none" aria-hidden="true">
      <path d="M0 0 Q10 30 120 38 Q220 44 290 30 Q200 42 100 44 Q20 44 0 40 Z" fill="var(--teal-mid)"/>
      <path d="M0 34 Q60 58 180 50 Q300 40 420 22 Q520 10 620 30 Q520 14 420 28 Q300 48 200 62 L200 70 L0 70 Z" fill="var(--teal)"/>
      <path d="M200 70 Q320 46 440 30 Q540 20 653 40 L653 70 Z" fill="var(--teal-pale)"/>
      <path d="M190 70 Q320 40 440 26 Q540 16 630 38" fill="none" stroke="var(--paper)" stroke-width="3"/>
    </svg>
  </section>

</body>
</html>
```